Modern business cards and stationery design for an IT company
Brolund Systems
Modern business cards and stationery design for an IT company - Information Technology
Creative Brief
Professional
Tomas Ellery
President
We do not want our address on the business card
tomas@brolundsys.example
www.brolundsys.example
BrolundSys BrolundSys
For reference, please visit our new website which is currently being constructed located at www.brolundsys.example/tellery This website provides the new design and layout for the company and potentially will help with the design process. Please note that the main website (www.brolundsys.example) is in process of being replaced with the first website mentioned. (www.brolundsys.example/tellery).

```html
<!DOCTYPE html>
<html lang="en">
<head>
<meta charset="utf-8">
<title>Brolund Systems – Business Card</title>
<link href="https://fonts.googleapis.com/css2?family=Montserrat:wght@400;500;600;700&display=swap" rel="stylesheet">
<style>
  :root {
    --bg: #e9e6e2;
    --card: #ffffff;
    --red: #d0101a;
    --red-dark: #8e0810;
    --grey: #b9bcc0;
    --grey-light: #dcdee1;
    --ink: #4a4d52;
    --white: #ffffff;
  }
  * { margin: 0; padding: 0; box-sizing: border-box; }
  html, body { width: 1200px; height: 901px; overflow: hidden; background: var(--bg); }
  body { font-family: "Montserrat", Arial, sans-serif; position: relative; }

  .business-card {
    position: absolute; left: 110px; top: 170px;
    width: 980px; height: 560px;
    background: var(--card);
    border-radius: 34px;
    overflow: hidden;
    box-shadow: 0 18px 40px rgba(0,0,0,0.18);
  }
  .card-swoosh { position: absolute; inset: 0; }

  .brand {
    position: absolute; left: 70px; top: 215px;
    display: flex; align-items: center; gap: 16px;
  }
  .brand-dot { width: 34px; height: 34px; border-radius: 50%; background: var(--red); }
  .brand-name {
    font-size: 36px; font-weight: 700; letter-spacing: 3px;
    color: var(--red); text-transform: uppercase; white-space: nowrap;
  }

  .person { position: absolute; left: 620px; top: 50px; }
  .person-name {
    font-size: 22px; font-weight: 600; color: var(--red);
    text-transform: uppercase; letter-spacing: 1px;
  }
  .person-title { font-size: 14px; color: var(--ink); margin-top: 4px; }

  .contact-list { position: absolute; left: 620px; top: 120px; list-style: none; }
  .contact-item {
    display: flex; align-items: center; gap: 14px;
    font-size: 15px; color: var(--ink); height: 28px; white-space: nowrap;
  }
  .contact-icon { width: 16px; height: 16px; fill: var(--red); flex: none; }
</style>
</head>
<body>
  <div class="business-card">
    <svg class="card-swoosh" width="980" height="560" viewBox="0 0 980 560">
      <defs>
        <linearGradient id="redBand" x1="0" y1="0" x2="1" y2="1">
          <stop offset="0" stop-color="#e3141f"/>
          <stop offset="0.6" stop-color="#c20c16"/>
          <stop offset="1" stop-color="#8e0810"/>
        </linearGradient>
        <linearGradient id="greyBand" x1="0" y1="0" x2="1" y2="0">
          <stop offset="0" stop-color="#dcdee1"/>
          <stop offset="1" stop-color="#a9adb2"/>
        </linearGradient>
      </defs>
      <path d="M0,370 C330,385 670,360 980,290 L980,560 L0,560 Z" fill="url(#greyBand)"/>
      <path d="M0,398 C340,410 690,385 980,318 L980,560 L0,560 Z" fill="url(#redBand)"/>
    </svg>

    <div class="brand">
      <span class="brand-dot"></span>
      <span class="brand-name">Brolund Systems</span>
    </div>

    <div class="person">
      <div class="person-name">Tomas Ellery</div>
      <div class="person-title">President</div>
    </div>

    <ul class="contact-list">
      <li class="contact-item">
        <svg class="contact-icon" viewBox="0 0 16 16"><path d="M3 1l3 3-1.5 2a9 9 0 0 0 5.5 5.5L12 10l3 3-2 2C7 15 1 9 1 3z"/></svg>
        012 555 0142
      </li>
      <li class="contact-item">
        <svg class="contact-icon" viewBox="0 0 16 16"><rect x="4" y="1" width="8" height="14" rx="1.5"/><rect x="5.5" y="3" width="5" height="8" fill="#fff"/></svg>
        012 555 0143
      </li>
      <li class="contact-item">
        <svg class="contact-icon" viewBox="0 0 16 16"><rect x="2" y="6" width="12" height="7" rx="1"/><rect x="4" y="2" width="8" height="4"/></svg>
        012 555 0144
      </li>
      <li class="contact-item">
        <svg class="contact-icon" viewBox="0 0 16 16"><rect x="1" y="3" width="14" height="10" rx="1"/><path d="M1.5 3.5L8 9l6.5-5.5" stroke="#fff" stroke-width="1.4" fill="none"/></svg>
        tomas@brolundsys.example
      </li>
      <li class="contact-item">
        <svg class="contact-icon" viewBox="0 0 16 16"><circle cx="8" cy="8" r="7"/><path d="M1 8h14M8 1c-3 3-3 11 0 14M8 1c3 3 3 11 0 14" stroke="#fff" stroke-width="1" fill="none"/></svg>
        www.brolundsys.example
      </li>
    </ul>
  </div>
</body>
</html>
```